Moonpetal Events

New Company ,I will attened clients personal residents(venu of there choice) and provide 3D ultra sound photos at time of ultra sound.This is a Non diagnostic ultra sound which does not replace the ultrasound reqested by Dr.The best time for ultra sound is 24 to 34 weeks.The baby sex can be kept confidential if requied and all cultral and diverse backgrounds cattered for..No referal requied for this.I have 2 main packges,1 baby shower and 2 family time.Extra options available are entertainment,Family time prior to baby shower for dad,decoration, Kids entertainment.
Contact number is 0477315842 email to be added ASAP.
prices start from $450

It Company

```html
<!DOCTYPE html>
<html lang="en">
<head>
<meta charset="utf-8">
<title>Moonpetal Events – Flyer</title>
<link rel="stylesheet" href="https://fonts.googleapis.com/css2?family=Oswald:wght@400;500;600&family=Arimo:wght@400&display=swap">
<style>
  :root {
    --magenta: #d81b72;
    --purple: #6a2a7c;
    --orange: #ee5a24;
    --pink-soft: #f3a6c8;
    --text-body: #2a3a5c;
    --white: #ffffff;
    --photo-top-a: #e9eef3;
    --photo-top-b: #cfd9e2;
    --skin-a: #e9c3a7;
    --skin-b: #c9957a;
    --scan-a: #c9772f;
    --scan-b: #6b3412;
  }
  html, body { margin: 0; padding: 0; overflow: hidden; background: var(--white); }
  .flyer {
    position: relative;
    width: 816px;
    height: 1200px;
    overflow: hidden;
    background: var(--white);
    font-family: "Oswald", sans-serif;
  }
  .exam-photo {
    position: absolute; left: 0; top: 0; width: 816px; height: 430px;
    background: linear-gradient(160deg, var(--photo-top-a) 0%, var(--photo-top-b) 55%, var(--skin-a) 100%);
  }
  .belly-photo {
    position: absolute; left: 0; top: 430px; width: 430px; height: 770px;
    background: linear-gradient(120deg, var(--skin-a) 0%, var(--skin-b) 70%, #f4e8e1 100%);
  }
  .scan-print {
    position: absolute; left: 68px; width: 235px; height: 165px;
    border: 7px solid var(--white);
    box-shadow: 0 3px 8px rgba(0,0,0,.25);
    background: radial-gradient(ellipse at 50% 45%, var(--scan-a) 0%, var(--scan-b) 80%);
  }
  .scan-print--one { top: 612px; transform: rotate(-2deg); }
  .scan-print--two { top: 792px; transform: rotate(1deg); }
  .scan-print--three { top: 972px; transform: rotate(-1deg); }
  .brand {
    position: absolute; left: 0; top: 130px; width: 816px;
    text-align: center;
  }
  .brand__name {
    display: inline-block;
    padding: 6px 22px;
    background: rgba(255,255,255,.85);
    color: var(--purple);
    font-weight: 500;
    font-size: 64px;
    line-height: 1.1;
  }
  .wave { position: absolute; left: 0; top: 340px; }
  .info {
    position: absolute; left: 430px; top: 452px; width: 386px;
    text-align: center;
  }
  .info__intro {
    margin: 0 14px 0 14px;
    font-family: "Arimo", sans-serif;
    font-size: 17px;
    line-height: 1.3;
    color: var(--text-body);
  }
  .packages { margin: 18px 0 0; }
  .packages__title {
    margin: 0; color: var(--orange);
    font-weight: 600; font-size: 34px; line-height: 1.25;
  }
  .packages__list { list-style: none; margin: 0 0 4px; padding: 0; }
  .packages__list li {
    color: var(--magenta); font-weight: 500;
    font-size: 23px; line-height: 1.45;
  }
  .contact {
    margin: 16px 0 0; color: var(--purple);
    font-weight: 600; font-size: 29px; line-height: 1.3;
    white-space: nowrap;
  }
  .price {
    margin-top: 22px;
    display: flex; align-items: center; justify-content: center; gap: 8px;
  }
  .price__label { color: var(--magenta); font-weight: 600; font-size: 36px; }
  .price__badge {
    width: 80px; height: 80px; border-radius: 50%;
    background: var(--magenta); color: var(--white);
    display: flex; align-items: center; justify-content: center;
    font-weight: 600; font-size: 30px;
  }
</style>
</head>
<body>
<div class="flyer">
  <div class="exam-photo" role="img" aria-label="Photo of a pregnant woman having an ultrasound scan with a clinician's gloved hands"></div>
  <div class="belly-photo" role="img" aria-label="Photo of a pregnant belly with hands holding ultrasound prints"></div>
  <div class="scan-print scan-print--one" role="img" aria-label="3D ultrasound photo of a baby"></div>
  <div class="scan-print scan-print--two" role="img" aria-label="3D ultrasound photo of a baby"></div>
  <div class="scan-print scan-print--three" role="img" aria-label="3D ultrasound photo of a baby"></div>

  <div class="brand"><span class="brand__name">Moonpetal Events</span></div>

  <svg class="wave" width="816" height="120" viewBox="0 0 816 120" aria-hidden="true">
    <path d="M0 60 C200 30 420 110 816 50 L816 120 L0 120 Z" fill="var(--white)"/>
    <path d="M0 44 C220 10 430 100 816 34 L816 56 C430 118 220 32 0 66 Z" fill="var(--magenta)"/>
    <path d="M0 66 C220 32 430 118 816 56 L816 64 C430 126 220 42 0 74 Z" fill="var(--purple)"/>
    <path d="M0 30 C220 0 430 86 816 24 L816 34 C430 100 220 10 0 44 Z" fill="var(--pink-soft)" opacity=".7"/>
  </svg>

  <section class="info">
    <p class="info__intro">A Non diagnostic ultra sound which does not replace the ultrasound reqested by Dr. The best time for ultra sound is 24 to 34 weeks. The baby sex can be kept confidential if required and all cultral and diverse backgrounds cattered for..No referal required for this</p>

    <div class="packages">
      <h2 class="packages__title">MAIN PACKAGES</h2>
      <ul class="packages__list">
        <li>BABY SHOWER</li>
        <li>FAMILY TIME</li>
      </ul>
      <h2 class="packages__title">EXTRA PACKAGES</h2>
      <ul class="packages__list">
        <li>ENTERTAINMENT</li>
        <li>FAMILY TIME PRIOR TO<br>BABY SHOWER FOR DAD</li>
        <li>DECORATION</li>
        <li>KIDS ENTERTAINMENT.</li>
      </ul>
    </div>

    <p class="contact">CALL 0477315842<br>OR EMAIL ----@MOONPETAL.COM</p>

    <div class="price">
      <span class="price__label">PRICES START AT</span>
      <span class="price__badge">$450</span>
    </div>
  </section>
</div>
</body>
</html>
```